Tranquil Pathway Business Card

Logo attached. (will be printing onto thick white/off white textured card)

Double sided business card for two Therapists working at Tranquil Pathway.

Require one design, but with different name and mobile numbers on each card.

Target Market(s)

Medical, Health

Industry/Entity Type

Business

Contact Information for Business Card

Need one business card design, but a separate card for each person - Colin Marchetti and Marieke de Boeckx.

FRONT OF CARD

Logo

Name (Colin Marchetti on one card, Marieke de Boeckx on the other)
Professional Clinical Hypnotherapist

Consulting Rooms (Near Lindqvist Hospital)
482 Brackenfield Road
Dunmore VIC 3987

Colin@TranquilPathway.example.au OR Marieke@TranquilPathway.example.au

Mobile: 0455 872 604 (for Colin) OR
Mobile: 0467 290 518 (for Marieke)

BACK OF CARD

Logo

Website: www.TranquilPathway.example.au

Phone: 1300 958 471

Requirements
Must have
• Text and logo only. No additiional graphics.

```html
<!DOCTYPE html>
<html lang="en">
<head>
<meta charset="utf-8">
<title>Tranquil Pathway Business Card</title>
<link href="https://fonts.googleapis.com/css2?family=Montserrat:wght@700&family=Roboto+Condensed:wght@400&display=swap" rel="stylesheet">
<style>
  :root {
    --navy: #1f1f86;
    --ink-on-navy: #6672a6;
    --ring-grey: #7b7d82;
    --paper: #ffffff;
    --stage: #e9e9ec;
    --back-ink: #3a3b48;
  }
  * { margin: 0; padding: 0; box-sizing: border-box; }
  html, body { width: 1200px; height: 1200px; overflow: hidden; background: var(--stage); }
  .canvas { position: relative; width: 1200px; height: 1200px; }

  .card { position: absolute; left: 180px; width: 840px; height: 480px; overflow: hidden; box-shadow: 0 6px 24px rgba(0,0,0,.18); }
  .card--front { top: 80px; background: var(--navy); }
  .card--back { top: 640px; background: var(--paper); }

  .front__person { position: absolute; left: 320px; top: 100px; font-family: "Roboto Condensed", sans-serif; color: var(--ink-on-navy); }
  .person__name { font-size: 25px; line-height: 1.1; }
  .person__role { font-size: 18px; line-height: 1.2; }

  .front__band { position: absolute; left: 0; top: 203px; width: 840px; height: 74px; background: var(--paper); }

  .brand { position: absolute; display: flex; align-items: center; }
  .brand__disc { flex: none; border-radius: 50%; background: var(--navy); border: solid var(--ring-grey); }
  .brand__rule { flex: none; background: var(--ring-grey); }
  .brand__name { font-family: "Montserrat", sans-serif; font-weight: 700; color: var(--navy); white-space: nowrap; text-transform: uppercase; letter-spacing: .5px; }

  .card--front .brand { left: 168px; top: 180px; height: 120px; }
  .card--front .brand__disc { width: 120px; height: 120px; border-width: 7px; }
  .card--front .brand__rule { width: 2px; height: 114px; margin: 0 16px 0 12px; }
  .card--front .brand__name { font-size: 33px; }

  .contact { position: absolute; font-family: "Roboto Condensed", sans-serif; list-style: none; }
  .contact li { display: flex; align-items: flex-start; }
  .contact svg { flex: none; }
  .card--front .contact { left: 320px; top: 312px; color: var(--ink-on-navy); font-size: 19px; line-height: 22px; }
  .card--front .contact svg { width: 16px; height: 16px; margin: 3px 8px 0 0; fill: none; stroke: var(--ink-on-navy); stroke-width: 1.6; }

  .card--back .brand { left: 232px; top: 340px; height: 60px; }
  .card--back .brand__disc { width: 56px; height: 56px; border-width: 4px; }
  .card--back .brand__rule { width: 1px; height: 52px; margin: 0 8px 0 6px; }
  .card--back .brand__name { font-size: 16px; }
  .card--back .contact { left: 500px; top: 346px; color: var(--back-ink); font-size: 12.5px; line-height: 18px; }
  .card--back .contact svg { width: 11px; height: 11px; margin: 3px 6px 0 0; fill: none; stroke: var(--back-ink); stroke-width: 1.6; }
</style>
</head>
<body>
<main class="canvas">

  <section class="card card--front" aria-label="Business card front">
    <div class="front__person">
      <p class="person__name">Marieke de Boeckx</p>
      <p class="person__role">Professional Clinical Hypnotherapist</p>
    </div>
    <div class="front__band"></div>
    <div class="brand">
      <span class="brand__disc"></span>
      <span class="brand__rule"></span>
      <span class="brand__name">Tranquil Pathway</span>
    </div>
    <ul class="contact">
      <li>
        <svg viewBox="0 0 16 16"><path d="M8 15s5-5 5-8.5A5 5 0 0 0 3 6.5C3 10 8 15 8 15z"/><circle cx="8" cy="6.5" r="1.8"/></svg>
        <span>Consulting Rooms (Near Lindqvist Hospital)<br>482 Brackenfield Road, Dunmore VIC 3987</span>
      </li>
      <li>
        <svg viewBox="0 0 16 16"><rect x="1.5" y="3.5" width="13" height="9"/><path d="M1.5 3.5 8 9l6.5-5.5"/></svg>
        <span>Marieke@TranquilPathway.example.au</span>
      </li>
      <li>
        <svg viewBox="0 0 16 16"><rect x="4.5" y="1.5" width="7" height="13" rx="1.5"/><path d="M7 12.3h2"/></svg>
        <span>0467 290 518</span>
      </li>
    </ul>
  </section>

  <section class="card card--back" aria-label="Business card back">
    <div class="brand">
      <span class="brand__disc"></span>
      <span class="brand__rule"></span>
      <span class="brand__name">Tranquil Pathway</span>
    </div>
    <ul class="contact">
      <li>
        <svg viewBox="0 0 16 16"><circle cx="8" cy="8" r="6.5"/><path d="M1.5 8h13M8 1.5c-3 3.5-3 9.5 0 13M8 1.5c3 3.5 3 9.5 0 13"/></svg>
        <span>www.TranquilPathway.example.au</span>
      </li>
      <li>
        <svg viewBox="0 0 16 16"><path d="M3 2h3l1.5 3.5-2 1.3a8 8 0 0 0 3.7 3.7l1.3-2L14 10v3a1.5 1.5 0 0 1-1.5 1.5A11 11 0 0 1 1.5 3.5 1.5 1.5 0 0 1 3 2z"/></svg>
        <span>1300 958 471</span>
      </li>
    </ul>
  </section>

</main>
</body>
</html>
```